The Lantern Pack! A Deck of cards to help you get over your ex.

I'm creating a deck of cards - 52 cards, 4 designs total. This contest is for the design of 4 cards, front and back. The winner will (most likely) be hired to fill out the other cards in the same style. I've included a template to give you a sense of what I imagine and also the physical sizes and specs of each card. (standard Poker size cards) I'll be creating about 20 different decks so there's a potential for you to be my long-term designer!

This is The Lantern Pack!

This deck of cards is designed to help you get over a breakup.
The idea is that after working through the deck, many of the stories and attachments to previous relationships will be resolved or broken.

There are 4 different sections, like the four suits in a Deck.
Each sections Addresses a different facet of relationships in general:

Blue - Your relationship with Yourself
Red - Your relationship to your partner
Purple - Your relationship to relationships
Green - Your relationship to your future

Each card:

FRONT - Headline (or theme) and a question
Back - A follow-up question and a QR code.
(QR code can be located anywhere on the back and will be unique to each card. It can also be a square shape or a round shape, your choice, and any color or a gradient.)

All other design elements are up to the artist.

They’re designed to give you an area to work on,
or present you with a conversation that might give you insights.
So the intention is that each of these cards is that you’ll do the work, or somehow take action on.

I’m looking for a feel that will work in a professional coaching
environment, or professional style-seminar or workshop.

I want people to feel like they want to carry around individual cards that speak to them in their wallets as a reminder, or post a card on their mirror as they work on a certain issue, or maybe glue a card into their journal.

So I’d like them to be visually appealing without going overboard.
Anything too plain, and the cards will look like cheap flash cards and won’t be valued.
Anything too elaborate, (like tarot-style illustrations) will take
away from the power of the question.
Updates

Low designer entries

Hello everyone! I've recieved a few good designs that give me some real hope that I'll find the right feel and deign for my coaching cards! However I would love to see some designs from some off the more experienced designers, so I've increased the prize amount and added a reward for second place! I've also extennded this project out for another 5 days to give more people a chance to submit their designs. If you have an idea, I'd love to see it! Happy designing!

Target Market(s)

Self-Help, Self-improvement, Relationship counselors, and people who are into transformational coaching.

Industry/Entity Type

Life Coaching

Font styles to use
Serif
Sans Serif

Colors
6b449b
0655a3
00a990
ec1f27

Requirements
Must have
• 1) A topic and a question on the front (with a darker background)
2) A question and a QR code on the back (with a ligher background)

One Blue card, one red card, one purple card and one green card.

The deck is a lantern pack, the theme is about getting over your ex, and that must communicate in the design.

The question must be the star of the card. The question must stand out on each side.
Nice to have
• Something that personalizes each card. Maybe even an illustration.
Should not have
• Overly simple, text only is too little.

Overly illustrated, like a tarot deck, is too much.

```html
<!DOCTYPE html>
<html lang="en">
<head>
<meta charset="utf-8">
<title>The Lantern Pack – Forgiveness</title>
<link rel="stylesheet" href="https://fonts.googleapis.com/css2?family=Poppins:wght@600&family=Playfair+Display:ital@1&display=swap">
<style>
  :root {
    --paper: #ffffff;
    --ink: #111111;
    --suit-green: #17aa94;
    --heading-text: #ffffff;
    --sketch-tone: #e6e6e6;
  }
  html, body {
    margin: 0;
    padding: 0;
    width: 1200px;
    height: 871px;
    overflow: hidden;
    background: var(--paper);
  }
  .card {
    position: relative;
    width: 1200px;
    height: 871px;
    background: var(--paper);
  }
  .cut-line {
    position: absolute;
    left: 22px;
    top: 24px;
    width: 1151px;
    height: 819px;
    box-sizing: border-box;
    border: 3px dashed var(--ink);
    border-radius: 44px;
  }
  .theme-band {
    position: absolute;
    left: 85px;
    top: 82px;
    width: 1024px;
    height: 273px;
  }
  .theme-band text {
    font-family: "Poppins", sans-serif;
    font-weight: 600;
    fill: var(--heading-text);
  }
  .question {
    position: absolute;
    left: 0;
    top: 470px;
    width: 1200px;
    margin: 0;
    text-align: center;
    font-family: "Playfair Display", serif;
    font-style: italic;
    font-weight: 400;
    font-size: 60px;
    line-height: 1;
    color: var(--ink);
  }
  .feather-sketch {
    position: absolute;
    left: 430px;
    top: 597px;
    width: 316px;
    height: 198px;
    border-radius: 50%;
    background: radial-gradient(ellipse at center, var(--sketch-tone), rgba(230,230,230,0) 70%);
  }
</style>
</head>
<body>
  <main class="card">
    <div class="cut-line"></div>

    <svg class="theme-band" viewBox="0 0 1024 273" aria-label="Forgiveness">
      <defs>
        <clipPath id="band-clip">
          <rect x="0" y="0" width="1024" height="273"/>
        </clipPath>
      </defs>
      <rect class="band-fill" x="0" y="0" width="1024" height="273" fill="var(--suit-green)"/>
      <g clip-path="url(#band-clip)">
        <text x="65" y="285" font-size="155" textLength="891" lengthAdjust="spacingAndGlyphs">FORGIVENESS</text>
      </g>
    </svg>

    <p class="question">What are you still holding on to?</p>

    <div class="feather-sketch" role="img" aria-label="Loose pencil sketch of a curled feather"></div>
  </main>
</body>
</html>
```